Brellin Trade Partners - we are Asian sourcing agents

We are sourcing agents based in the USA and we act as sourcing agents for clients in throughout the world. We focus primarily on custom sewn goods. So basically companies who do not have the in-house expertise to do it themselves, come to us and have us find suitable factories in Asia to do the production. We are middlemen. We find the factories...quote the project...manage the quality control and then deliver the goods directly to our customer's door. We pride ourselves in making the communication very easy and precise.

Current page is www.brellintrade.example

I am not happy w/ the overall look. The spacing...the photos, the fonts...the design elements...the pictures. I want a cool, crisp design that conveys professionalism and clearly depicts/explains what we do.

Requirements
Must have
• use my logo....I like it...it was designed by someone on this website.
Nice to have
• a video/animation of the entire process would be wonderful. Showing initial contact with our office in the USA...then to my correspondence with my offices in Taiwan and in Hong Kong...and then back and fort w/ the customer.....and then between my people in Hong Kong/Taiwan with the local factories......and then a quote is generated and sent to my client......to samples being made and sent for approval.....to a PO being generated......to final samples being sent.....to the order being shipped and delivered to the clients warehouse. I was thinking of an animation showing arrows and text showing the back and forth communication and explaining how the process flows.

```html
<!DOCTYPE html>
<html lang="en">
<head>
<meta charset="utf-8">
<title>Brellin Trade Partners</title>
<link href="https://fonts.googleapis.com/css2?family=Open+Sans:wght@400;600&family=Arimo:wght@400;700&display=swap" rel="stylesheet">
<style>
:root{
  --navy:#101c5c;
  --green:#7a9a23;
  --grey-bar:#e4e4e4;
  --side-bg:#e8e8e8;
  --side-line:#ffffff;
  --text:#333333;
  --blue:#1d3a8a;
  --white:#ffffff;
}
*{margin:0;padding:0;box-sizing:border-box}
html,body{width:784px;height:1200px;overflow:hidden;background:var(--white)}
body{position:relative;font-family:Arimo,Arial,sans-serif;color:var(--text)}
.abs{position:absolute}
.topbar{left:0;top:0;width:784px;height:18px;background:var(--navy)}
.topbar .links{right:73px;top:4px;font-size:8px;color:#c9d0ff}
.brand{left:74px;top:34px;display:flex;align-items:center;gap:8px}
.brand .mark{width:44px;height:44px;border-radius:50%;background:var(--navy)}
.brand .name{font-family:"Open Sans",sans-serif;font-weight:600;font-size:17px;color:var(--navy);line-height:1.1}
.brand .sub{font-size:7px;letter-spacing:.8px;color:#555;margin-top:3px}
.quote-btn{left:554px;top:42px;width:148px;height:31px;background:#111;border-radius:3px;color:#fff;font-family:"Open Sans",sans-serif;font-size:13px;display:flex;align-items:center;justify-content:center;gap:12px}
.nav{left:0;top:95px;width:784px;height:31px;background:var(--green)}
.nav a{position:absolute;top:0;height:31px;line-height:31px;color:#fff;font-family:"Open Sans",sans-serif;font-weight:600;font-size:10.5px;text-decoration:none;transform:translateX(-50%)}
.nav .sep{position:absolute;top:6px;width:1px;height:19px;background:rgba(255,255,255,.45)}
.nav .social{position:absolute;top:8px;width:16px;height:16px;border-radius:50%;background:#fff}
.perks{left:0;top:126px;width:784px;height:26px;background:var(--grey-bar);font-size:9px;color:#444}
.perks span{position:absolute;top:8px;transform:translateX(-50%);white-space:nowrap}
.hero{left:66px;top:173px;width:652px;height:301px;background:linear-gradient(100deg,#b7a79a 0%,#d9cfc6 35%,#ece6e0 60%,#c9b3a4 100%)}
.hero-box{left:74px;top:253px;width:307px;height:165px;background:rgba(225,225,225,.88);padding:13px 10px 0 10px}
.hero-box h1{font-family:Arimo,sans-serif;font-weight:700;font-size:19.5px;color:#111;letter-spacing:-.4px}
.hero-box h2{font-family:Arimo,sans-serif;font-weight:400;font-size:13px;color:var(--blue);margin-top:5px}
.hero-box p{font-size:10px;line-height:14.4px;margin-top:9px;color:#444;padding-left:2px;width:285px}
.side-head{left:66px;width:190px;height:31px;background:var(--green);color:#fff;font-family:"Open Sans",sans-serif;font-size:13px;line-height:31px;padding-left:13px}
.side-list{left:66px;width:190px;background:var(--side-bg);list-style:none}
.side-list li{height:23.6px;line-height:23.6px;font-size:9.2px;color:#222;padding-left:12px;border-bottom:1px solid var(--side-line)}
.side-list li::before{content:"+";margin-right:8px}
.section-title{font-family:"Open Sans",sans-serif;font-weight:400;color:#1a2450}
.rule{height:1px;background:#ccc}
.tile{width:120px;height:97px;display:flex;align-items:center;justify-content:center}
.tile .label{background:var(--green);color:#fff;font-family:"Open Sans",sans-serif;font-size:17px;padding:1px 8px;letter-spacing:.3px}
.about p{font-size:11.2px;line-height:16.3px;color:#333;letter-spacing:.15px}
.footer{left:0;top:975px;width:784px;height:199px;background:var(--navy);color:#fff}
.footer h3{position:absolute;top:26px;font-family:"Open Sans",sans-serif;font-weight:600;font-size:13.5px}
.contact-row{position:absolute;left:68px;display:flex;align-items:flex-start;gap:8px;font-size:8.5px;line-height:12px}
.contact-row svg{flex:none}
.tweet{position:absolute;left:242px;font-size:7.8px;line-height:10.5px;width:150px}
.tweet b{font-weight:700}
.tweet .h{color:#aab0d0}
.tweet .u{color:#6fb7ff}
.about-links{position:absolute;left:410px;top:57px;list-style:none;font-size:8.5px}
.about-links li{height:19.6px}
.follow{position:absolute;left:568px;top:53px;width:154px;font-size:8.5px;line-height:13px;text-align:justify}
.sq{position:absolute;top:127px;width:20px;height:20px;background:#d8d8d8}
.bottom{left:0;top:1174px;width:784px;height:26px;background:var(--green);color:#fff;font-size:9px}
.bottom span{position:absolute;top:8px}
</style>
</head>
<body>

<div class="abs topbar"><span class="abs links">My Account &nbsp;|&nbsp; Check Out</span></div>

<div class="abs brand">
  <div class="mark"></div>
  <div>
    <div class="name">Brellin Trade Partners</div>
    <div class="sub">USA · HONG KONG · TAIPEI</div>
  </div>
</div>

<div class="abs quote-btn">Request Quote
  <svg width="7" height="10" viewBox="0 0 7 10"><path d="M1 1l4 4-4 4" stroke="#fff" stroke-width="1.6" fill="none"/></svg>
</div>

<nav class="abs nav">
  <a style="left:94px">Home</a><span class="sep" style="left:134px"></span>
  <a style="left:175px">Production</a><span class="sep" style="left:221px"></span>
  <a style="left:268px">Categories</a><span class="sep" style="left:313px"></span>
  <a style="left:356px">About Us</a><span class="sep" style="left:397px"></span>
  <a style="left:438px">Request</a><span class="sep" style="left:476px"></span>
  <a style="left:513px">Quote</a>
  <span class="social" style="left:607px"></span>
  <span class="social" style="left:628px"></span>
  <span class="social" style="left:649px"></span>
  <span class="social" style="left:670px"></span>
  <span class="social" style="left:691px"></span>
</nav>

<div class="abs perks">
  <svg class="abs" style="left:126px;top:8px" width="14" height="10" viewBox="0 0 14 10"><rect x="1" y="1" width="12" height="7" fill="none" stroke="#888"/></svg>
  <span style="left:184px">Customer service</span>
  <svg class="abs" style="left:295px;top:8px" width="12" height="10" viewBox="0 0 12 10"><path d="M11 9C9 4 6 4 4 4V1L0 5l4 4V6c3 0 5 1 7 3z" fill="none" stroke="#888"/></svg>
  <span style="left:380px">3 Days Money Back Gaurantee</span>
  <svg class="abs" style="left:521px;top:8px" width="10" height="10" viewBox="0 0 10 10"><path d="M5 0l1.5 3.3 3.5.4-2.6 2.4.7 3.5L5 7.8 1.9 9.6l.7-3.5L0 3.7l3.5-.4z" fill="#999"/></svg>
  <span style="left:606px">5% Discount on order over $199</span>
</div>

<div class="abs hero" role="img" aria-label="Photo of a woman at a sewing machine working on red fabric, with garments hanging behind her"></div>
<div class="abs hero-box">
  <h1>Asian Outsourcing Made Easy!</h1>
  <h2>Sourcing custom goods in china</h2>
  <p>We outsource sewing services direct from China. Our long-es-tablished and extensive network of offshore factory-partners provides our clients with access to a wide variety of contract sewing expertise from Chinese manufacturers. Clients only need to communicate with our US agents.Asia.</p>
</div>

<div class="abs side-head" style="top:501px">SOURCING SOLUTIONS</div>
<ul class="abs side-list" style="top:532px;height:197px;padding-top:8px">
  <li>Bags</li><li>Cases</li><li>Covers</li><li>Gloves</li><li>Medical</li><li>Sewn Goods</li><li>Sporting Goods</li>
</ul>
<div class="abs side-head" style="top:730px">SOURCING SOLUTIONS</div>
<ul class="abs side-list" style="top:762px;height:174px;padding-top:8px">
  <li>Contract Sewing in China</li><li>What is the Process?</li><li>What the Minimum Order?</li><li>Contract Outsourcing FAQ</li><li>Outsourcing Case Study</li><li>Custom Industrial Sewing in China</li>
</ul>

<h2 class="abs section-title" style="left:296px;top:500px;font-size:21px">Our Products</h2>
<div class="abs rule" style="left:296px;top:531px;width:422px"></div>

<div class="abs tile" style="left:296px;top:545px;background:#8aab35;border:2px solid #dcdcdc" role="img" aria-label="Photo of a messenger bag"><span class="label" style="background:none">BAGS</span></div>
<div class="abs tile" style="left:449px;top:545px;background:linear-gradient(160deg,#e4e4e4,#b9bccb)" role="img" aria-label="Photo of a covered motorcycle"><span class="label">COVER</span></div>
<div class="abs tile" style="left:598px;top:545px;background:linear-gradient(160deg,#ececec,#c8c8c8)" role="img" aria-label="Photo of work gloves"><span class="label">GLOVES</span></div>
<div class="abs tile" style="left:296px;top:676px;background:linear-gradient(160deg,#e8e8e8,#b8a8a8)" role="img" aria-label="Photo of sport shoes"><span class="label">SHOPPING</span></div>
<div class="abs tile" style="left:450px;top:676px;background:linear-gradient(90deg,#4d4fa0,#8a4aa8,#c0306a,#c84030)" role="img" aria-label="Photo of coloured phone cases"><span class="label">CASES</span></div>
<div class="abs tile" style="left:600px;top:676px;background:linear-gradient(160deg,#c9a79a,#b23a34)" role="img" aria-label="Photo of a sewing machine stitching red cloth"><span class="label">SEWN</span></div>

<h2 class="abs section-title" style="left:293px;top:795px;font-size:17px;color:#111">Don’t go it alone</h2>
<div class="abs rule" style="left:293px;top:825px;width:427px"></div>
<div class="abs about" style="left:294px;top:832px;width:424px">
  <p>Brellin Trade Partners has been sourcing custom sewn goods in Asia since 1998. We work with our clients by matching their unique production needs with the best possible China sewing factories. We manage the entire process from start to finish, by first identifying the best factories to quote each job. The next step is negotiating the best (fair) price possible. We complete the process by monitoring the quality of the goods.</p>
</div>

<footer class="abs footer">
  <h3 style="left:68px">Contact us</h3>
  <h3 style="left:241px">Latest Feed</h3>
  <h3 style="left:411px">About Us</h3>
  <h3 style="left:568px">Follow Us</h3>

  <div class="contact-row" style="top:58px">
    <svg width="14" height="14" viewBox="0 0 14 14"><circle cx="7" cy="7" r="6" fill="none" stroke="#fff"/><path d="M5 4l1 2-1 1c.5 1 1 1.5 2 2l1-1 2 1-1 1.5C6 10 4 8 3.5 5.5z" fill="#fff"/></svg>
    <span style="margin-top:1px">04 8820 1147 (Phone)</span></div>
  <div class="contact-row" style="top:89px">
    <svg width="14" height="12" viewBox="0 0 14 12"><rect x="3" y="0" width="8" height="4" fill="#fff"/><rect x="0" y="4" width="14" height="6" rx="1" fill="#fff"/><rect x="3" y="8" width="8" height="4" fill="#fff" stroke="#101c5c"/></svg>
    <span>04 8820 1147 (Fax)</span></div>
  <div class="contact-row" style="top:121px">
    <svg width="14" height="10" viewBox="0 0 14 10"><rect x=".5" y=".5" width="13" height="9" fill="#fff"/><path d="M.5 .5L7 6l6.5-5.5" stroke="#101c5c" fill="none"/></svg>
    <span>admin@brellintrade.example</span></div>
  <div class="contact-row" style="top:149px">
    <svg width="12" height="15" viewBox="0 0 12 15"><path d="M6 0a6 6 0 0 0-6 6c0 4 6 9 6 9s6-5 6-9a6 6 0 0 0-6-6z" fill="#fff"/><circle cx="6" cy="6" r="2.2" fill="#101c5c"/></svg>
    <span>PO Box : 4420, Harbour Row Lorem<br>ipsum dollor si5170</span></div>

  <div class="tweet" style="top:52px"><b>Marisol</b> <span class="h">@threadnote</span><br>How to Download Photos from Feed<br>to... <span class="u">brl.example/Q7tnWpa</span></div>
  <div class="tweet" style="top:95px"><b>Marisol</b> <span class="h">@threadnote</span><br>How to Download Photos from Feed<br>to... <span class="u">brl.example/Q7tnWpa</span></div>
  <div class="tweet" style="top:138px"><b>Marisol</b> <span class="h">@threadnote</span><br>How to Download Photos from Feed<br>to... <span class="u">brl.example/Q7tnWpa</span></div>

  <ul class="about-links">
    <li>Investor</li><li>Careers</li><li>Terms &amp; Conditions of Services</li><li>Privacy Policy</li><li>Services Level Agreement</li><li>Master Commerical Agfrement</li>
  </ul>

  <p class="follow">Lorem Ipsum is simply dummy text of the printing and typesetting industry. Lorem Ipsum has been the industry's standard dummy text ever since the 1500s,</p>
  <span class="sq" style="left:571px"></span>
  <span class="sq" style="left:597px"></span>
  <span class="sq" style="left:622px"></span>
  <span class="sq" style="left:648px"></span>
  <span class="sq" style="left:673px"></span>
  <span class="sq" style="left:699px"></span>
</footer>

<div class="abs bottom">
  <span style="left:68px">© Copyright 2015, Brellin Trade Partners. Inc. All rights reserved.</span>
  <span style="right:71px">Site Map | Legal | Privacy | Cookies</span>
</div>

</body>
</html>
```